Online store for a printing company

we are a printing company and want a webshop in spotify.
With our full catalog, customer login, online payments, choices of paper types etc.

https://www.velmora.be --> like this one, we have the same products/catalogus so you can take them.

Ofcourse you don't need to add all the 500 products. But if you add like 30-50 we will add the rest.

our current site is; www.lindevaart.be

Target Market(s)

B2B / B2C

Requirements
Must have
• *full catalog
*costumer login
*online payments
Nice to have
• products in the picture banner

```html
<!DOCTYPE html>
<html lang="en">
<head>
<meta charset="utf-8">
<title>Lindevaart – Printing Webshop</title>
<link href="https://fonts.googleapis.com/css2?family=Heebo:wght@400;500;700;800&display=swap" rel="stylesheet">
<style>
:root{
  --accent:#e8461e;
  --ink:#111111;
  --text:#2a2a2a;
  --paper:#ffffff;
  --blush:#f4efee;
  --footer:#1b1b1b;
  --footer-text:#d6d6d6;
  --rule:#8a8a8a;
}
*{box-sizing:border-box;margin:0;padding:0}
html,body{width:1200px;height:3534px;overflow:hidden}
body{position:relative;background:var(--paper);font-family:'Heebo',sans-serif;color:var(--text)}
.abs{position:absolute}
.btn{position:absolute;background:var(--accent);color:#fff;font-weight:500;display:flex;align-items:center;justify-content:center;text-transform:uppercase;letter-spacing:.2px}

/* header */
.site-header{top:0;left:0;width:1200px;height:100px;background:var(--paper)}
.brand{left:133px;top:7px;width:82px;height:82px;border-radius:50%;background:var(--ink);color:#fff;display:flex;flex-direction:column;align-items:center;justify-content:center;font-weight:700;font-size:15px;line-height:1}
.brand small{font-size:6px;font-weight:400;margin-top:4px}
.main-nav a{position:absolute;top:38px;font-size:14.5px;color:var(--ink);text-decoration:none;letter-spacing:.2px}
.main-nav a.current{font-weight:700;text-decoration:underline;text-underline-offset:4px}
.cart{left:1026px;top:32px}
.cart-count{left:1051px;top:30px;width:18px;height:18px;border-radius:50%;background:var(--accent);color:#fff;font-size:11px;font-weight:700;display:flex;align-items:center;justify-content:center}

/* hero */
.hero{top:100px;left:0;width:1200px;height:645px;background:linear-gradient(100deg,#1c2230 0%,#2c3a55 25%,#4a4f5a 45%,#8a4a2a 65%,#b8652a 78%,#3a2a28 100%)}
.hero-title{left:131px;top:298px;font-size:64px;font-weight:800;color:#fff;letter-spacing:2px;line-height:1}
.hero-sub{left:132px;top:390px;font-size:19px;font-weight:700;color:#fff;line-height:28px;text-transform:uppercase}
.hero .btn,.hero-btn{left:133px;top:466px;width:148px;height:48px;font-size:19px}
.slider-arrows{left:1104px;top:678px}

/* headings */
.section-title{position:absolute;left:0;width:1200px;text-align:center;font-size:25px;font-weight:800;color:var(--ink);text-transform:uppercase}
.title-rule{position:absolute;left:576px;width:48px;height:2px;background:var(--rule)}

/* categories */
.cat-card{position:absolute;top:857px;width:300px}
.cat-card .photo{width:300px;height:226px}
.card-name{position:absolute;left:0;width:100%;text-align:center;font-size:16px;font-weight:700;color:var(--ink);text-transform:uppercase}
.card-text{position:absolute;left:0;width:100%;text-align:center;font-size:13.5px;line-height:20px;color:var(--text)}

/* recommended */
.recommended{top:1301px;left:0;width:1200px;height:483px;background:var(--blush)}
.product{position:absolute;top:1432px;width:223px}
.product .photo{width:223px;height:242px}
.product .name{margin-top:20px;font-size:12.5px;font-weight:700;color:var(--ink);text-transform:uppercase}
.product .price{margin-top:3px;font-size:14px;font-weight:700;color:var(--ink)}

/* banner */
.banner{top:1784px;left:0;width:1200px;height:527px;background:linear-gradient(160deg,#5a5d63 0%,#3c3f45 50%,#2a2c30 100%)}
.banner-title{left:0;top:1960px;width:1200px;text-align:center;font-size:46px;font-weight:800;color:#fff;line-height:61px;text-transform:uppercase}

/* testimonials */
.quote{left:330px;top:2443px;width:540px;text-align:center;font-size:16px;line-height:22.5px;color:var(--text)}
.quote-name{left:0;top:2593px;width:1200px;text-align:center;font-size:14px;font-weight:700;color:var(--ink)}

/* best sellers */
.bestsellers{top:2663px;left:0;width:1200px;height:565px;background:var(--blush)}
.best-card{position:absolute;top:2784px;width:300px;height:406px;background:var(--paper)}
.best-card .photo{width:300px;height:217px}

/* footer */
.site-footer{top:3228px;left:0;width:1200px;height:306px;background:var(--footer);color:var(--footer-text)}
.footer-head{position:absolute;top:3270px;font-size:16px;font-weight:700;color:#fff;text-transform:uppercase}
.footer-text{position:absolute;font-size:13.5px;line-height:20.5px;color:var(--footer-text)}
.footer-menu a{display:block;color:var(--footer-text);text-decoration:none;font-size:13.5px;line-height:21px;text-transform:uppercase}
.newsletter{left:724px;top:3348px;width:340px;height:46px;border:1.5px solid #fff;display:flex}
.newsletter span{flex:1;padding-left:17px;font-size:12px;color:#cfcfcf;display:flex;align-items:center}
.newsletter b{width:47px;background:var(--accent);display:flex;align-items:center;justify-content:center}
.footer-rule{left:128px;top:3448px;width:940px;height:1px;background:#3a3a3a}
.copyright{left:128px;top:3482px;font-size:12.5px;color:var(--footer-text)}
.pay{position:absolute;top:3476px;width:45px;height:28px;border-radius:3px}
</style>
</head>
<body>

<header class="site-header abs">
  <div class="brand abs">Lindevaart<small>drukwerk &amp; ontwerp</small></div>
  <nav class="main-nav">
    <a class="current" href="#" style="left:418px">HOME</a>
    <a href="#" style="left:494px">ABOUT US</a>
    <a href="#" style="left:596px">PRODUCTS</a>
    <a href="#" style="left:699px">BLOG</a>
    <a href="#" style="left:766px">CONTACT US</a>
    <a href="#" style="left:877px">CUSTOMER LOGIN</a>
  </nav>
  <svg class="cart abs" width="32" height="30" viewBox="0 0 32 30" fill="none" stroke="#111" stroke-width="2">
    <path d="M1 3h5l4 17h16l4-12H8"/><circle cx="12" cy="26" r="2"/><circle cx="24" cy="26" r="2"/>
    <path d="M10 12h18M11 16h15" stroke-width="1.5"/>
  </svg>
  <div class="cart-count abs">0</div>
</header>

<section class="hero abs" role="img" aria-label="Large format printer printing a colourful city poster"></section>
<h1 class="hero-title abs">PRINTING</h1>
<p class="hero-sub abs">Lorem ipsum is simply dummy<br>text of the printing</p>
<a class="btn hero-btn">Shop now</a>
<svg class="slider-arrows abs" width="46" height="26" viewBox="0 0 46 26" fill="none" stroke="#fff" stroke-width="2.5">
  <path d="M12 3 4 13l8 10"/><path d="M34 3l8 10-8 10"/>
</svg>

<h2 class="section-title" style="top:785px">Categories</h2>

<article class="cat-card" style="left:132px">
  <div class="photo" role="img" aria-label="Folded business brochures on a wooden table" style="background:linear-gradient(135deg,#c9c6c2,#8e9aa6)"></div>
  <h3 class="card-name" style="top:253px">Broucher</h3>
  <p class="card-text" style="top:289px">Lorem Ipsum is simply dummy text of the<br>printing and typesetting industry.</p>
  <a class="btn" style="left:99px;top:351px;width:111px;height:36px;font-size:14px">Shop now</a>
</article>
<article class="cat-card" style="left:451px">
  <div class="photo" role="img" aria-label="Green printed fabric face masks" style="background:linear-gradient(135deg,#f1f1f0,#1f5a48)"></div>
  <h3 class="card-name" style="top:253px">Printing</h3>
  <p class="card-text" style="top:289px">Lorem Ipsum is simply dummy text of the<br>printing and typesetting industry.</p>
  <a class="btn" style="left:93px;top:351px;width:111px;height:36px;font-size:14px">Shop now</a>
</article>
<article class="cat-card" style="left:771px">
  <div class="photo" role="img" aria-label="Stack of printed magazines" style="background:linear-gradient(160deg,#e8e8ea,#5a6578)"></div>
  <h3 class="card-name" style="top:253px">Books</h3>
  <p class="card-text" style="top:289px">Lorem Ipsum is simply dummy text of the<br>printing and typesetting industry.</p>
  <a class="btn" style="left:98px;top:351px;width:111px;height:36px;font-size:14px">Shop now</a>
</article>

<section class="recommended abs"></section>
<h2 class="section-title" style="top:1340px;text-transform:uppercase">Recommended for you</h2>
<div class="title-rule" style="top:1387px"></div>

<article class="product" style="left:133px">
  <div class="photo" role="img" aria-label="Open printed catalogue" style="background:linear-gradient(135deg,#f2f2f2,#9a7a52)"></div>
  <p class="name">Lorem ipsum is simply</p><p class="price">$25.00</p>
</article>
<article class="product" style="left:377px">
  <div class="photo" role="img" aria-label="Business cards on grey stone" style="background:linear-gradient(135deg,#7a7a78,#d8d8d6)"></div>
  <p class="name">Lorem ipsum is simply</p><p class="price">$25.00</p>
</article>
<article class="product" style="left:613px">
  <div class="photo" role="img" aria-label="Embroidered patch on a black garment" style="background:linear-gradient(135deg,#2a2a2a,#3d3d44)"></div>
  <p class="name">Lorem ipsum is simply</p><p class="price">$25.00</p>
</article>
<article class="product" style="left:848px">
  <div class="photo" role="img" aria-label="Printed white mug with blue handle" style="background:linear-gradient(135deg,#3a5478,#e6e8ea)"></div>
  <p class="name">Lorem ipsum is simply</p><p class="price">$25.00</p>
</article>

<section class="banner abs" role="img" aria-label="Stacks of printed books on a production line"></section>
<h2 class="banner-title abs">Design is thinking<br>made visual</h2>

<h2 class="section-title" style="top:2360px">Testimonials</h2>
<div class="title-rule" style="top:2406px"></div>
<p class="quote abs">At vero eos et accusamus et iusto odio dignissimos ducimus qui blanditiis praesentium voluptatum deleniti atque corrupti quos dolores et quas molestias excepturi sint occaecati cupiditate non provident, similique sunt in culpa qui officia deserunt mollitia animi, id est laborum et dolorum fuga. Et harum quidem rerum facilis est et expedita</p>
<p class="quote-name abs">RICHARD</p>

<section class="bestsellers abs"></section>
<h2 class="section-title" style="top:2699px">Best sellers</h2>
<div class="title-rule" style="top:2746px"></div>

<article class="best-card" style="left:132px">
  <div class="photo" role="img" aria-label="Printed black and white motorcycle t-shirts" style="background:linear-gradient(135deg,#6fb8a8,#1d1d1d 50%,#f2f2f2)"></div>
  <h3 class="card-name" style="top:243px">Lorem ipsum is simply</h3>
  <p class="card-text" style="top:282px">Lorem Ipsum is simply dummy text of the<br>printing and typesetting industry.</p>
  <a class="btn" style="left:92px;top:344px;width:118px;height:35px;font-size:14px">Shop now</a>
</article>
<article class="best-card" style="left:451px">
  <div class="photo" role="img" aria-label="Black and white business card set" style="background:linear-gradient(135deg,#f4f4f4,#3a3a3a 55%,#e8e8e8)"></div>
  <h3 class="card-name" style="top:243px">Lorem ipsum is simply</h3>
  <p class="card-text" style="top:282px">Lorem Ipsum is simply dummy text of the<br>printing and typesetting industry.</p>
  <a class="btn" style="left:92px;top:344px;width:118px;height:35px;font-size:14px">Shop now</a>
</article>
<article class="best-card" style="left:771px">
  <div class="photo" role="img" aria-label="Yellow and black sports flyers" style="background:linear-gradient(90deg,#f2e01c 50%,#1a1a1a 50%)"></div>
  <h3 class="card-name" style="top:243px">Lorem ipsum is simply</h3>
  <p class="card-text" style="top:282px">Lorem Ipsum is simply dummy text of the<br>printing and typesetting industry.</p>
  <a class="btn" style="left:99px;top:344px;width:118px;height:35px;font-size:14px">Shop now</a>
</article>

<footer class="site-footer abs"></footer>
<h4 class="footer-head" style="left:132px">About</h4>
<p class="footer-text" style="left:132px;top:3307px;width:290px">Lorem Ipsum is simply dummy text of the printing and typesetting industry. veritatis et qai architecto beatae vitae dicta sunt explicabo. Nemo enim ipsam</p>
<h4 class="footer-head" style="left:498px">Menu</h4>
<nav class="footer-menu abs" style="left:498px;top:3302px">
  <a href="#">Home</a><a href="#">About us</a><a href="#">Products</a><a href="#">Blog</a><a href="#">Contact us</a>
</nav>
<h4 class="footer-head" style="left:724px">Stay connected</h4>
<p class="footer-text" style="left:724px;top:3302px">Join our mailing list to get updates</p>
<div class="newsletter abs"><span>E mail address</span><b><svg width="12" height="18" viewBox="0 0 12 18" fill="none" stroke="#fff" stroke-width="2"><path d="M2 2l7 7-7 7"/></svg></b></div>
<div class="footer-rule abs"></div>
<p class="copyright abs">Copyright © 2021 All Rights Reserved</p>
<div class="pay" style="left:864px;background:#2b3f8f"></div>
<div class="pay" style="left:916px;background:#2448a8"></div>
<div class="pay" style="left:969px;background:#3a3a4a"></div>
<div class="pay" style="left:1022px;background:#2a7ac8"></div>

</body>
</html>
```